Re design and optimization of a website for pension Ora Vahi, a b&b in Tahiti, French Polynesia.

We have a website already : www.pensionoravahi.example

The general idea is to create a new site that is colorful, young and with an exotic, tropical feel since we are on a beautiful island.

The website will be in three languages, all the text is already available on our website, nothing changes.

All pages must have the name of the website (pension ora vahi b&b) our address, mail and phone number
It would be nice to have a link to our mail from every page

Sections have to be easy to update : text and pics

The sections needed are :

- Home page (accueil)

- Prices (tarifs)

- Bookings (reservations) = link to our mailbox : pensionoravahi@post.example )

- Pictures : in three separate categories that will pop up on this page : 1/ pics of the b&b 2/ pics of the surroundings 3/ customer's pics (we'll give new pics, not the current ones)

- Map of Tahiti : we'd like one map that we'll give you and also a Google map with our location, date and local time would be great

- Links (liens)

We let you see what would look best for the top banner and the switches, matching the logo and the pictures, make it nice and tropical !!
We have a few layouts that we did, maybe you will have a better idea of what we want by looking at them, if you can use them and have a good overall feel

We'd like to remind you guys that Tahiti is a dream destination, so you have to come up with something that the visitors will go : wow !!

We cater for backpackers to mid range accommodations and families, it all about a relaxed friendly atmosphere here !

NOTE THAT WE DON'T KNOW MUCH ABOUT PROGRAMMING AND CODING SO IT AS TO BE READY TO GO ON-LINE, ALL YOUR HELP IS APPRECIATED !!!
Also in Tahiti, the
INTERNET is quite low bandwidth so optimization is a must !

P.S : Live demo of the homepage is welcome ;)

We are available to all you for extra infos, good luck

regards,

remy & Pension Ora Vahi

Target Market(s)

Families and couples : individual rooms

Backpackers : Dormitories

people looking for an authentic stay in a familial environment

Customers of all ages and all nationalities

Requirements
Must have
• You must insist on the main page about :
the easy beach access
the breakfast included (with French baguette !)
Airport pick up 24/7
Many activities departing from our place : scuba diving, canyoning, 4x4 tour, rental cars, surf school, para-glide....

Please find a great way to highlight these !

```html
<!DOCTYPE html>
<html lang="en">
<head>
<meta charset="utf-8">
<title>Pension Ora Vahi - Bed and Breakfast</title>
<link href="https://fonts.googleapis.com/css2?family=Arimo:ital,wght@0,400;0,700;1,400;1,700&display=swap" rel="stylesheet">
<style>
:root{
  --sky-top:#5fb6ea;
  --sky-mid:#b9e3f5;
  --sea:#4fa9c4;
  --sand:#efe0c8;
  --panel-top:#e6f5ff;
  --panel-bottom:#2f9fe6;
  --panel-border:#1b6fb4;
  --frame-white:#ffffff;
  --ink:#1a2230;
  --content-top:rgba(78,96,104,.82);
  --content-bottom:rgba(118,108,98,.92);
  --board-top:#f7d58c;
  --board-bottom:#d98f2a;
  --board-edge:#8b5a1a;
  --tick:#3fbf2a;
  --link:#1a2a60;
}
*{box-sizing:border-box;margin:0;padding:0}
html,body{width:815px;height:1200px;overflow:hidden}
body{
  position:relative;
  font-family:"Arimo",Arial,sans-serif;
  color:var(--ink);
  background:
    radial-gradient(ellipse 180px 420px at 0 300px,rgba(63,138,42,.55),transparent 70%),
    radial-gradient(ellipse 180px 420px at 815px 700px,rgba(63,138,42,.5),transparent 70%),
    linear-gradient(180deg,var(--sky-top) 0,var(--sky-mid) 330px,var(--sea) 420px,#8fd0d8 560px,var(--sand) 720px,#f3e6d2 1200px);
}
.page-backdrop{position:absolute;inset:0}

/* header */
.site-header{
  position:absolute;left:87px;top:24px;width:672px;height:128px;
  border-radius:10px;overflow:hidden;
  box-shadow:0 3px 8px rgba(0,0,0,.45);
}
.brand{
  position:absolute;left:0;top:0;width:300px;height:128px;
  display:flex;flex-direction:column;justify-content:center;padding-left:12px;
  background:linear-gradient(180deg,rgba(160,190,220,.9),rgba(90,120,150,.95));
}
.brand-name{font-size:33px;font-weight:700;color:#fff;line-height:1.05;white-space:nowrap}
.brand-tag{font-size:20px;font-weight:700;color:#fff;margin-top:4px;letter-spacing:1px}
.header-photo{position:absolute;left:300px;top:0;right:0;bottom:0;
  background:linear-gradient(135deg,#d8a758 0,#c48a3c 45%,#8a5a2e 70%,#e5c892 100%)}
.lang-switch{position:absolute;top:10px;left:640px;display:flex;gap:4px}
.lang-flag{width:34px;height:27px;border-radius:2px;box-shadow:0 1px 2px rgba(0,0,0,.4)}
.flag-en{background:linear-gradient(180deg,#22407a,#c8102e 50%,#22407a)}
.flag-fr{background:linear-gradient(90deg,#2248a0 33%,#fff 33% 66%,#d62828 66%)}
.flag-es{background:linear-gradient(180deg,#c8102e 25%,#f5c400 25% 75%,#c8102e 75%)}

/* blue panels */
.info-panel{
  position:absolute;top:163px;width:179px;height:196px;overflow:hidden;
  border:1px solid var(--panel-border);border-radius:8px;
  background:linear-gradient(180deg,var(--panel-top),#6ec1f2 55%,var(--panel-bottom));
  box-shadow:0 2px 5px rgba(0,0,0,.35);
  font-size:11px;line-height:1.15;
}
.highlights{left:87px;padding:5px 4px 0 7px}
.highlights-title{text-align:center;margin-bottom:8px}
.highlights-list{list-style:none}
.highlights-list li{position:relative;padding-left:18px;margin-bottom:9px}
.highlights-list li:last-child{margin-bottom:0}
.highlights-list li svg{position:absolute;left:0;top:0}

.contact{left:579px;padding:6px 6px 0}
.contact-title{text-align:center;font-size:14px;font-weight:400;margin-bottom:7px}
.contact-row{display:flex;align-items:center;gap:6px;margin-bottom:5px;min-height:24px}
.contact-row a{color:var(--link);font-size:10.5px}
.contact-icon{flex:0 0 24px}
.contact-address{text-align:center;margin-top:3px}

/* slideshow */
.slideshow{position:absolute;left:277px;top:163px;width:293px;height:195px}
.slide-photo{position:absolute;left:31px;top:8px;width:231px;height:180px;border-radius:50%;
  border:7px solid var(--frame-white);
  background:linear-gradient(180deg,#8ec9ef 0,#b8e1f3 40%,#3a7a3a 48%,#d9c9a6 70%,#c8b48a 100%)}
.slide-arrow{position:absolute;top:93px}
.slide-prev{left:6px}.slide-next{right:6px}

/* side panels */
.side-panel{
  position:absolute;left:87px;width:179px;
  border:5px solid var(--frame-white);border-radius:6px;
  box-shadow:0 1px 4px rgba(0,0,0,.25);
}
.menu-panel{top:367px;height:257px;
  background:linear-gradient(180deg,#6bb7d6,#9ad3e0 50%,#e2d8c4)}
.menu-title{text-align:center;color:#fff;font-weight:700;font-style:italic;font-size:14px;letter-spacing:1px;margin:11px 0 6px;text-shadow:0 1px 2px rgba(0,0,0,.5)}
.menu-list{list-style:none;padding:0 8px}
.menu-list li{margin-bottom:6.6px}
.menu-list a{
  display:block;height:26px;line-height:26px;text-align:center;color:#fff;
  text-decoration:none;font-size:12.5px;text-shadow:0 1px 1px rgba(0,0,0,.5);
  border-radius:50%;border:1px solid var(--board-edge);
  background:linear-gradient(180deg,var(--board-top),var(--board-bottom));
}
.map-panel{top:632px;height:228px;background:linear-gradient(180deg,#bfe2f6,#92cdee)}
.panel-heading{text-align:center;color:#fff;font-style:italic;font-size:14px;margin-top:12px;text-shadow:0 1px 1px rgba(0,80,140,.5)}
.map-thumb{margin:11px auto 0;width:149px;height:129px;border-radius:4px;
  background:radial-gradient(ellipse 45% 55% at 40% 45%,#4d7a3a,#2f5a3a 60%,#1c3a5c 75%,#16305a)}
.map-button{display:block;margin:14px auto 0;width:92px;height:19px;font:12px "Arimo",Arial,sans-serif;
  background:linear-gradient(180deg,#fff,#e4e4e4);border:1px solid #aaa;border-radius:2px;color:var(--ink)}
.reservation-panel{top:868px;height:257px;background:linear-gradient(180deg,#cfe9f8,#a9d9f1)}
.reservation-panel .panel-heading{margin-top:6px}
.reservation-form{padding:4px 9px 0}
.reservation-form input,.reservation-form textarea{
  display:block;width:152px;height:31px;margin-bottom:3px;border:1px solid #c9c9c9;border-radius:4px;
  background:linear-gradient(180deg,#fff,#f1f1f1);font:12px "Arimo",Arial,sans-serif;color:#555;padding:0 10px}
.reservation-form textarea{height:126px;padding:8px;resize:none}
.reservation-form button{display:block;margin:2px auto 0;width:70px;height:17px;font:12px "Arimo",Arial,sans-serif;
  background:linear-gradient(180deg,#fff,#e4e4e4);border:1px solid #aaa;border-radius:2px}

/* main content */
.main-content{
  position:absolute;left:271px;top:369px;width:489px;height:758px;border-radius:8px;
  background:linear-gradient(180deg,var(--content-top),var(--content-bottom) 45%,rgba(120,110,100,.95));
  color:#fff;font-size:11.5px;line-height:1.17;text-align:center;
}
.content-title{font-size:14px;font-weight:400;margin-top:30px}
.intro{margin:12px 42px 0}
.intro+.intro{margin-top:14px}
.houses-title{margin-top:35px}
.features{list-style:none;text-align:left;margin:26px 0 0 66px}
.features li{position:relative;padding-left:14px}
.features li svg{position:absolute;left:0;top:2px}
.feature-oval{
  position:absolute;top:336px;height:245px;border-radius:50%;
  border:6px solid var(--frame-white);
  display:flex;flex-direction:column;justify-content:flex-start;
  padding-top:28px;
}
.oval-surf{left:10px;width:147px}
.oval-beach{left:165px;width:151px;padding-top:26px}
.oval-nearby{left:328px;width:155px;padding-top:48px}
.oval-gap{height:14px}
.diver-art{position:absolute;left:332px;top:613px;width:151px;height:122px;border-radius:40% 50% 45% 55%;
  background:radial-gradient(ellipse at 50% 55%,#3a4a52,#5f6f74 55%,rgba(120,110,100,0) 75%)}

/* footer */
.site-footer{
  position:absolute;left:90px;top:1133px;width:670px;height:59px;border-radius:8px;
  border:1px solid var(--panel-border);
  background:linear-gradient(180deg,var(--panel-top),#6ec1f2 55%,var(--panel-bottom));
  box-shadow:0 2px 5px rgba(0,0,0,.35);font-size:11.5px;
}
.copyright{position:absolute;left:7px;top:14px;text-align:center;line-height:1.17}
.footer-nav{position:absolute;left:195px;top:20px}
.footer-nav a{color:var(--link)}
.social{position:absolute;left:525px;top:5px;width:140px;text-align:center}
.social-links{display:flex;justify-content:center;gap:8px;margin-top:6px}
.social-links span{display:flex;align-items:center;gap:3px;font-size:10.5px;color:var(--ink)}
.social-links i{display:block;width:10px;height:10px;background:#1f4f9a}
</style>
</head>
<body>
<div class="page-backdrop" role="img" aria-label="Tropical beach backdrop with palm leaves, sea and sand"></div>

<header class="site-header">
  <div class="header-photo" role="img" aria-label="Photo of the pension terrace lounge with sofa and cushions"></div>
  <div class="brand">
    <span class="brand-name">Pension Ora Vahi</span>
    <span class="brand-tag">bed and breakfast</span>
  </div>
</header>
<nav class="lang-switch" aria-label="Languages">
  <span class="lang-flag flag-en" role="img" aria-label="English"></span>
  <span class="lang-flag flag-fr" role="img" aria-label="French"></span>
  <span class="lang-flag flag-es" role="img" aria-label="Spanish"></span>
</nav>

<aside class="info-panel highlights">
  <p class="highlights-title">Many activities departing from our place</p>
  <ul class="highlights-list">
    <li><svg width="13" height="13" viewBox="0 0 13 13"><g stroke="#fff" stroke-width="1.6"><path d="M6.5 0v13M0 6.5h13M2 2l9 9M11 2l-9 9"/></g></svg>Breakfast included (with French baguette)!</li>
    <li><svg width="13" height="13" viewBox="0 0 13 13"><g stroke="#fff" stroke-width="1.6"><path d="M6.5 0v13M0 6.5h13M2 2l9 9M11 2l-9 9"/></g></svg>Airport pick up 24/7</li>
    <li><svg width="13" height="13" viewBox="0 0 13 13"><g stroke="#fff" stroke-width="1.6"><path d="M6.5 0v13M0 6.5h13M2 2l9 9M11 2l-9 9"/></g></svg>Easy beach access</li>
    <li><svg width="13" height="13" viewBox="0 0 13 13"><g stroke="#fff" stroke-width="1.6"><path d="M6.5 0v13M0 6.5h13M2 2l9 9M11 2l-9 9"/></g></svg>Many activities departing from our place : scuba diving, canyoning, 4x4 tour, rental cars, surf school, para-glide and more!</li>
  </ul>
</aside>

<section class="slideshow">
  <div class="slide-photo" role="img" aria-label="Photo of a white sand beach with trees and lagoon"></div>
  <svg class="slide-arrow slide-prev" width="16" height="16" viewBox="0 0 16 16"><circle cx="8" cy="8" r="7.5" fill="#111" stroke="#fff"/><path d="M9.5 4.5 6 8l3.5 3.5" fill="none" stroke="#fff" stroke-width="1.8"/></svg>
  <svg class="slide-arrow slide-next" width="16" height="16" viewBox="0 0 16 16"><circle cx="8" cy="8" r="7.5" fill="#111" stroke="#fff"/><path d="M6.5 4.5 10 8l-3.5 3.5" fill="none" stroke="#fff" stroke-width="1.8"/></svg>
</section>

<aside class="info-panel contact">
  <h2 class="contact-title">Contact us</h2>
  <div class="contact-row">
    <svg class="contact-icon" width="24" height="24" viewBox="0 0 26 26"><path d="M5 3c2-1 4 4 3 5s-2 1 0 5 5 7 7 6 2-2 3-1 4 3 2 5-7 1-11-5S3 4 5 3z" fill="#d0181a"/></svg>
    <span>(00) 40 12 34<br>(00) 689 70 11 22</span>
  </div>
  <div class="contact-row">
    <svg class="contact-icon" width="24" height="20" viewBox="0 0 26 22"><rect x="2" y="4" width="22" height="15" rx="2" fill="#fff3cf" stroke="#b88a2e"/><path d="M2 5l11 8 11-8" fill="none" stroke="#b88a2e"/></svg>
    <a href="mailto:pensionoravahi@post.example">pensionoravahi@<wbr>post.example</a>
  </div>
  <div class="contact-row">
    <svg class="contact-icon" width="24" height="24" viewBox="0 0 26 26"><circle cx="13" cy="13" r="10" fill="#2a8ee0"/><circle cx="13" cy="13" r="5" fill="#bfe4ff"/></svg>
    <a href="#">www.pensionoravahi<wbr>.example</a>
  </div>
  <p class="contact-address">Pension Ora Vahi<br>BP 100200 Ravaiti 98700 Fare Nui TAHITI, French Polynesia</p>
</aside>

<nav class="side-panel menu-panel">
  <p class="menu-title">MENU</p>
  <ul class="menu-list">
    <li><a href="#">Home</a></li>
    <li><a href="#">Prices</a></li>
    <li><a href="#">Bookings</a></li>
    <li><a href="#">Pictures</a></li>
    <li><a href="#">Map of Tahiti</a></li>
    <li><a href="#">Links</a></li>
  </ul>
</nav>

<aside class="side-panel map-panel">
  <p class="panel-heading">Map of Tahiti</p>
  <div class="map-thumb" role="img" aria-label="Satellite map of Tahiti island"></div>
  <button class="map-button" type="button">See large map</button>
</aside>

<aside class="side-panel reservation-panel">
  <p class="panel-heading">Quick Reservation</p>
  <form class="reservation-form">
    <input type="text" placeholder="Your Name">
    <input type="email" placeholder="Your Email">
    <textarea placeholder="Message"></textarea>
    <button type="button">Send</button>
  </form>
</aside>

<main class="main-content">
  <h1 class="content-title">Pension Ora Vahi - Bed and Breakfast</h1>
  <p class="intro">is located in the Paea district - 18,6 kms from Papeete - mountain side and 200 meters from the nicest white sand beach of Tahiti French Polynesia</p>
  <p class="intro">With a friendly atmosphere - breakfast included every morning at the terrace in the garden<br>self - service between 7h30 to 10h30 with a fantastic view at the mountain...</p>
  <p class="houses-title">PENSION ORA VAHI consists of 3 houses with :</p>
  <ul class="features">
    <li><svg width="11" height="10" viewBox="0 0 11 10"><path d="M1 5l3 3 6-7" fill="none" stroke="var(--tick)" stroke-width="2.2"/></svg>1 Reception (tel - fax - internet)</li>
    <li><svg width="11" height="10" viewBox="0 0 11 10"><path d="M1 5l3 3 6-7" fill="none" stroke="var(--tick)" stroke-width="2.2"/></svg>5 rooms (individual or familial rooms)</li>
    <li><svg width="11" height="10" viewBox="0 0 11 10"><path d="M1 5l3 3 6-7" fill="none" stroke="var(--tick)" stroke-width="2.2"/></svg>2 dorms(4 beds in each)</li>
    <li><svg width="11" height="10" viewBox="0 0 11 10"><path d="M1 5l3 3 6-7" fill="none" stroke="var(--tick)" stroke-width="2.2"/></svg>cooking facilities (gas stoves, fridges, micro-waves, plates and cutlery)</li>
    <li><svg width="11" height="10" viewBox="0 0 11 10"><path d="M1 5l3 3 6-7" fill="none" stroke="var(--tick)" stroke-width="2.2"/></svg>communal bathrooms</li>
    <li><svg width="11" height="10" viewBox="0 0 11 10"><path d="M1 5l3 3 6-7" fill="none" stroke="var(--tick)" stroke-width="2.2"/></svg>television and library</li>
    <li><svg width="11" height="10" viewBox="0 0 11 10"><path d="M1 5l3 3 6-7" fill="none" stroke="var(--tick)" stroke-width="2.2"/></svg>many terraces - large gardens (hammocks, lounging area)</li>
    <li><svg width="11" height="10" viewBox="0 0 11 10"><path d="M1 5l3 3 6-7" fill="none" stroke="var(--tick)" stroke-width="2.2"/></svg>easy beach access (at 200 meters away)</li>
  </ul>

  <div class="feature-oval oval-surf">
    <p>Accessible surf<br>spots include</p>
    <div class="oval-gap"></div>
    <p>Sapinus, mairie of<br>Paea, Papara,<br>Teahupoo...</p>
    <div class="oval-gap"></div>
    <p>Also departing from the<br>pension:<br>- scuba diving trips<br>- 4WD tours of the<br>island<br>-surf school<br>- paragliding</p>
  </div>
  <div class="feature-oval oval-beach">
    <p>Public beach</p>
    <div class="oval-gap"></div>
    <p>With amenities<br>only 200 meters away!<br>"Vai Lagoon Park"<br>also featuring :</p>
    <div class="oval-gap"></div>
    <p>- restaurant<br>- snack bar<br>- picnic area<br>- kids play area<br>- Ideal for snorkeling</p>
  </div>
  <div class="feature-oval oval-nearby">
    <p>Within proximity</p>
    <div class="oval-gap"></div>
    <p>- Rental cars and<br>scooters<br>- shops<br>- supermarkets<br>- snacks - restaurants<br>- medical center<br>and more!</p>
  </div>
  <div class="diver-art" role="img" aria-label="Illustration of a scuba diver"></div>
</main>

<footer class="site-footer">
  <p class="copyright">Copyright © "Pension Ora Vahi"<br>All rights reserved. 2012</p>
  <nav class="footer-nav"><a href="#">Home</a> | <a href="#">Prices</a> | <a href="#">Bookings</a> | <a href="#">Pictures</a> | <a href="#">Map of Tahiti</a> | <a href="#">Links</a></nav>
  <div class="social">
    <p>See our social pages in</p>
    <div class="social-links"><span><i></i>Friendbook</span><span><i></i>Chirper</span></div>
  </div>
</footer>
</body>
</html>
```